Hearing Specialists Need a Billboard Advertisement Designed

We need an advertisement that will stretch across the windows on the back of our office. Total size is 17 1/2 ft wide x 9 1/2 ft high. This would serve as a billboard for our office to the main road that passes behind and will be printed on perforated vinyl. We would like to communicate that we provide hearing services for all ages (newborn through senior). We would like the advertisement to feature people of a variety of ages and ethnicities. We would also like "Achieve your best hearing" to be a part of the design, and our phone number 803-471-3962. Our colors are blue and we want our advertisement to convey professional/medical level care that also feels current and welcoming for patients of all ages.

Target Market(s)

Older active adults with hearing loss/concerns and parents of children who have hearing loss.

Industry/Entity Type

Office

Font styles to use
Sans Serif
Script

Colors
0392cd

Requirements
Must have
• Picture of people of all ages.

```html
<!DOCTYPE html>
<html lang="en">
<head>
<meta charset="utf-8">
<title>Harborview Hearing Billboard</title>
<link rel="stylesheet" href="https://fonts.googleapis.com/css2?family=Roboto:wght@300;900&family=Montserrat:wght@400&display=swap">
<style>
  :root {
    --brand-blue: #0a8db6;
    --brand-blue-deep: #067aa2;
    --accent-cyan: #1ef2f6;
    --edge-cyan: #63d6f2;
    --phone-cyan: #8fe4f6;
    --white: #ffffff;
  }
  html, body {
    margin: 0;
    padding: 0;
    width: 1200px;
    height: 652px;
    overflow: hidden;
    background: #ffffff;
  }
  .billboard {
    position: relative;
    width: 1200px;
    height: 652px;
    overflow: hidden;
    background: radial-gradient(ellipse at 75% 55%, var(--brand-blue) 0%, var(--brand-blue-deep) 100%);
  }
  .people-photo {
    position: absolute;
    inset: 0;
    width: 1200px;
    height: 652px;
  }
  .brand {
    position: absolute;
    left: 686px;
    top: 50px;
    display: flex;
    align-items: center;
    gap: 16px;
    color: var(--white);
    font-family: "Montserrat", sans-serif;
    font-weight: 400;
    font-size: 25px;
    letter-spacing: 6px;
    text-transform: uppercase;
  }
  .brand-dot {
    width: 34px;
    height: 34px;
    border-radius: 50%;
    background: var(--white);
  }
  .headline {
    position: absolute;
    left: 690px;
    width: 480px;
    top: 136px;
    margin: 0;
    text-align: center;
    font-family: "Roboto", sans-serif;
    font-weight: 900;
    font-size: 100px;
    line-height: 86px;
    text-transform: uppercase;
  }
  .headline-line { display: block; }
  .headline-white { color: var(--white); }
  .headline-cyan { color: var(--accent-cyan); }
  .headline-gap { margin-top: 12px; }
  .phone {
    position: absolute;
    left: 706px;
    top: 560px;
    display: flex;
    align-items: center;
    gap: 18px;
    color: var(--phone-cyan);
    font-family: "Roboto", sans-serif;
    font-weight: 300;
    font-size: 52px;
  }
  .phone-icon { width: 44px; height: 44px; }
</style>
</head>
<body>
  <main class="billboard">
    <svg class="people-photo" viewBox="0 0 1200 652" aria-hidden="false">
      <defs>
        <linearGradient id="photoTones" x1="0" y1="0" x2="1" y2="1">
          <stop offset="0" stop-color="#2a2a2c"/>
          <stop offset="0.45" stop-color="#b8876d"/>
          <stop offset="0.75" stop-color="#d9b26a"/>
          <stop offset="1" stop-color="#c85a3a"/>
        </linearGradient>
      </defs>
      <path d="M0 0 H556 C630 110 676 240 664 340 C654 450 590 570 494 652 H0 Z" fill="none" stroke="var(--edge-cyan)" stroke-width="16"/>
      <path role="img" aria-label="Photo of a smiling group of people of all ages and ethnicities, from toddlers to seniors, giving thumbs up" d="M0 0 H556 C630 110 676 240 664 340 C654 450 590 570 494 652 H0 Z" fill="url(#photoTones)"/>
    </svg>

    <div class="brand">
      <span class="brand-dot"></span>
      <span class="brand-name">Harborview Hearing</span>
    </div>

    <h1 class="headline">
      <span class="headline-line headline-white">Achieve</span>
      <span class="headline-line headline-white">Your</span>
      <span class="headline-line headline-cyan headline-gap">Best</span>
      <span class="headline-line headline-cyan">Hearing</span>
    </h1>

    <div class="phone">
      <svg class="phone-icon" viewBox="0 0 24 24" aria-hidden="true">
        <path fill="var(--phone-cyan)" d="M6.6 10.8c1.4 2.8 3.8 5.1 6.6 6.6l2.2-2.2c.3-.3.7-.4 1-.2 1.1.4 2.3.6 3.6.6.6 0 1 .4 1 1V20c0 .6-.4 1-1 1C10.6 21 3 13.4 3 4c0-.6.4-1 1-1h3.5c.6 0 1 .4 1 1 0 1.3.2 2.5.6 3.6.1.3 0 .7-.2 1z"/>
      </svg>
      <span class="phone-number">803-471-3962</span>
    </div>
  </main>
</body>
</html>
```